Whitmore Business Card Design

The name of the business is Dara Whitmore, CPA LLC
The service that we offer is Accounting, Tax & Consulting Services. I need it to have the following items:
Dara Whitmore, Principal
Phone Number
Email Address
Physical Address

I have attached the company logo, one in black and one in white. Please provide a design in black background and the other in white background. Please include "Accounting, Tax & Consulting Services". I want the business card to be clean and very professional.

```html
<!DOCTYPE html>
<html lang="en">
<head>
<meta charset="utf-8">
<title>Dara Whitmore, CPA LLC – Business Card</title>
<link href="https://fonts.googleapis.com/css2?family=Montserrat:wght@500;600&family=Roboto:wght@400;500;700&display=swap" rel="stylesheet">
<style>
  :root {
    --page: #d9d9d9;
    --card: #000000;
    --white: #ffffff;
    --red: #a51d21;
    --grey: #5a5a5a;
    --grey-light: #b5b5b5;
  }
  * { box-sizing: border-box; margin: 0; padding: 0; }
  html, body { width: 1200px; height: 900px; overflow: hidden; background: var(--page); }
  .canvas { position: relative; width: 1200px; height: 900px; }
  .card {
    position: absolute; left: 233px; width: 702px; height: 400px;
    background: var(--card);
    box-shadow: 0 4px 14px rgba(0,0,0,0.25);
    overflow: hidden;
  }
  .card--front { top: 43px; }
  .card--back { top: 459px; }

  /* front */
  .front-brand {
    position: absolute; left: 0; right: 0; top: 240px;
    text-align: center; color: var(--white);
  }
  .front-brand__name {
    font-family: "Montserrat", sans-serif; font-weight: 600;
    font-size: 42px; letter-spacing: 0.5px;
  }
  .front-brand__title {
    margin-top: 6px;
    font-family: "Montserrat", sans-serif; font-weight: 600;
    font-size: 28px; letter-spacing: 2.6px;
  }

  /* back */
  .back-brand { position: absolute; left: 17px; top: 118px; }
  .back-brand__name {
    font-family: "Montserrat", sans-serif; font-weight: 500;
    font-size: 19px; color: var(--grey); letter-spacing: 0.3px;
  }
  .back-brand__title {
    margin-top: 3px;
    font-family: "Montserrat", sans-serif; font-weight: 500;
    font-size: 12.5px; color: var(--grey-light); letter-spacing: 1.4px;
  }
  .person { position: absolute; right: 17px; top: 18px; text-align: right; }
  .person__name {
    font-family: "Roboto", sans-serif; font-weight: 700;
    font-size: 29px; color: var(--white); letter-spacing: -0.3px;
  }
  .person__role {
    font-family: "Roboto", sans-serif; font-weight: 500;
    font-size: 19px; color: var(--red); margin-top: 1px;
  }
  .services {
    position: absolute; left: 18px; top: 208px;
    font-family: "Roboto", sans-serif; font-weight: 700;
    font-size: 24px; color: var(--red); letter-spacing: 4.4px;
    white-space: nowrap;
  }
  .services-rule {
    position: absolute; left: 17px; width: 668px; top: 246px;
    height: 3px; background: var(--white);
  }
  .contact {
    position: absolute; display: flex; align-items: flex-start; gap: 14px;
    font-family: "Roboto", sans-serif; font-weight: 500;
    font-size: 23px; color: var(--white); line-height: 27px;
  }
  .contact--phone { left: 19px; top: 282px; }
  .contact--email { left: 19px; top: 326px; }
  .contact--address { left: 358px; top: 283px; }
  .icon { width: 31px; height: 31px; flex: none; margin-top: -2px; }
</style>
</head>
<body>
<div class="canvas">

  <section class="card card--front">
    <div class="front-brand">
      <div class="front-brand__name">Dara Whitmore, CPA LLC</div>
      <div class="front-brand__title">CERTIFIED PUBLIC ACCOUNTANT</div>
    </div>
  </section>

  <section class="card card--back">
    <div class="back-brand">
      <div class="back-brand__name">Dara Whitmore, CPA LLC</div>
      <div class="back-brand__title">CERTIFIED PUBLIC ACCOUNTANT</div>
    </div>

    <div class="person">
      <div class="person__name">Dara Whitmore</div>
      <div class="person__role">Principal</div>
    </div>

    <div class="services">ACCOUNTING, TAX &amp; CONSULTING SERVICES</div>
    <div class="services-rule"></div>

    <div class="contact contact--phone">
      <svg class="icon" viewBox="0 0 32 32" aria-hidden="true">
        <circle cx="16" cy="16" r="15" fill="#fff" stroke="#ccc" stroke-width="1.5"/>
        <path d="M11.5 8.5l2.8-.6 1.6 4-1.8 1.4c.8 1.9 2.3 3.5 4.2 4.4l1.5-1.8 4 1.7-.6 2.8c-.2.8-1 1.3-1.8 1.2C15 20.8 10.2 16 9.5 10.3c-.1-.8.4-1.6 1.2-1.8z" fill="var(--red)"/>
      </svg>
      <span>(555) 214-0198</span>
    </div>

    <div class="contact contact--email">
      <svg class="icon" viewBox="0 0 32 32" aria-hidden="true">
        <circle cx="16" cy="16" r="15" fill="#fff" stroke="#ccc" stroke-width="1.5"/>
        <rect x="8.5" y="10.5" width="15" height="11" rx="1.2" fill="var(--red)"/>
        <path d="M9 11.5l7 5.5 7-5.5M9 20.5l5-4.2M23 20.5l-5-4.2" stroke="#fff" stroke-width="1.2" fill="none"/>
      </svg>
      <span>info@whitmorecpa.com</span>
    </div>

    <div class="contact contact--address">
      <svg class="icon" viewBox="0 0 32 32" aria-hidden="true">
        <circle cx="16" cy="16" r="15" fill="#fff" stroke="#ccc" stroke-width="1.5"/>
        <path d="M16 7.5c-3.4 0-6 2.6-6 5.9 0 4.3 6 11.1 6 11.1s6-6.8 6-11.1c0-3.300-2.6-5.9-6-5.9z" fill="var(--red)"/>
        <circle cx="16" cy="13.4" r="2.2" fill="#fff"/>
      </svg>
      <span>421, Address line goes here<br>45552, Country Name</span>
    </div>
  </section>

</div>
</body>
</html>
```